Banner Ad Design Project -Oil and Gas Value Chain

I am needing to create a simple graphic like the one here:

size: 720x300
http://craftpanelhub.example/designresources/banners/examples/720x300.php

Oil and Gas Value Chain:
The oil industry has three levels: upstream, midstream, and downstream which encompass the main segments in the supply chain. The upstream level includes the exploration, drilling, and production of crude oil and the midstream level includes the transportation and trading of crude oil to refineries. The downstream level refers to the refining of crude oil into finished product, the storage of crude oil, and the distribution and marketing of crude oil to wholesalers and retailers.

http://www.fuelvistaplan.example/images/value_chain.gif
http://www.crudelearnhub.example/modules/m008/imgs/fig_001.jpg
Here is another that is more for reference:

http://www.halvern.example/web/soc142/team9/GVC_clip_image002.jpg

https://www.findora.example/search?q=oil+value+chain&hl=en&tbo=u&prmd=imvns&tbm=isch&source=univ&sa=X&ei=I1hsUOuEC-SK2wXry4DAAg&ved=0CDMQsAQ&biw=1680&bih=925

```html
<!DOCTYPE html>
<html lang="en">
<head>
<meta charset="utf-8">
<title>Oil Supply Chain</title>
<link rel="stylesheet" href="https://fonts.googleapis.com/css2?family=Carlito:wght@700&display=swap">
<style>
  :root {
    --ink: #000000;
    --paper: #ffffff;
    --band-light: #b9c9dc;
    --band-light-edge: #a9bbd2;
    --band-blue: #1f4f9e;
    --band-blue-deep: #163e84;
    --label-navy: #1b2436;
    --caption: #1a1a1a;
  }
  html, body {
    margin: 0;
    padding: 0;
    width: 1200px;
    height: 500px;
    overflow: hidden;
    background: var(--paper);
  }
  .banner {
    position: relative;
    width: 1200px;
    height: 500px;
    box-sizing: border-box;
    border: 5px solid var(--ink);
    background: var(--band-light);
    font-family: "Carlito", "Calibri", sans-serif;
    font-weight: 700;
    overflow: hidden;
  }
  .banner-title {
    position: absolute;
    left: 0; top: 0;
    width: 100%;
    height: 60px;
    margin: 0;
    background: var(--ink);
    color: var(--paper);
    font-size: 50px;
    line-height: 60px;
    text-align: center;
    letter-spacing: 1px;
  }
  .stage-labels {
    position: absolute;
    left: 0; top: 60px;
    width: 100%;
    height: 65px;
    background: linear-gradient(var(--band-light), var(--band-light-edge));
  }
  .stage-label {
    position: absolute;
    top: 0;
    width: 343px;
    margin: 0;
    font-size: 40px;
    line-height: 68px;
    text-align: center;
    color: var(--label-navy);
    text-shadow: 1px 2px 2px rgba(0,0,0,0.35);
  }
  .stage-strip {
    position: absolute;
    left: 0; top: 125px;
    width: 100%;
    height: 257px;
    background: radial-gradient(ellipse at center, var(--band-blue) 0%, var(--band-blue-deep) 100%);
  }
  .stage-photo {
    position: absolute;
    top: 13px;
    width: 343px;
    height: 235px;
    box-sizing: border-box;
    border: 2px solid #0c2250;
  }
  .photo-upstream { left: 32px; background: linear-gradient(#d9e2ea 0%, #c5d0d6 50%, #6f8f3e 62%, #5d7f33 100%); }
  .photo-midstream { left: 423px; background: linear-gradient(#8b8a9a 0%, #c59a86 40%, #6b6c7a 65%, #2f3440 100%); }
  .photo-downstream { left: 815px; background: linear-gradient(#aec9e6 0%, #cfd8df 45%, #b84a3c 50%, #d7cfc0 60%, #7a7c80 100%); }
  .stage-captions {
    position: absolute;
    left: 0; top: 382px;
    width: 100%;
    height: 108px;
  }
  .stage-caption {
    position: absolute;
    top: 8px;
    width: 343px;
    margin: 0;
    font-size: 34px;
    line-height: 44px;
    text-align: center;
    color: var(--caption);
  }
  .col-up { left: 32px; }
  .col-mid { left: 423px; }
  .col-down { left: 815px; }
  .flow-arrows {
    position: absolute;
    left: 0; top: 0;
    width: 1190px;
    height: 490px;
    pointer-events: none;
  }
</style>
</head>
<body>
<div class="banner">
  <h1 class="banner-title">OIL SUPPLY CHAIN</h1>

  <div class="stage-labels">
    <h2 class="stage-label col-up">UPSTREAM</h2>
    <h2 class="stage-label col-mid">MIDSTREAM</h2>
    <h2 class="stage-label col-down">DOWNSTREAM</h2>
  </div>

  <div class="stage-strip">
    <div class="stage-photo photo-upstream" role="img" aria-label="Oil derrick on a grassy field with trees"></div>
    <div class="stage-photo photo-midstream" role="img" aria-label="Refinery with smokestacks at dusk"></div>
    <div class="stage-photo photo-downstream" role="img" aria-label="Roadside fuel station forecourt"></div>
  </div>

  <div class="stage-captions">
    <p class="stage-caption col-up">Exploration &amp;<br>Production</p>
    <p class="stage-caption col-mid">Transportation &amp;<br>Refining / Processing</p>
    <p class="stage-caption col-down">Distribution &amp;<br>Retail Sale</p>
  </div>

  <svg class="flow-arrows" viewBox="0 0 1190 490" aria-hidden="true">
    <g class="arrow-up-to-mid">
      <path d="M315 200 Q420 105 540 215" fill="none" stroke="#fff" stroke-width="22"/>
      <polygon points="568,240 520,236 558,194" fill="#fff" stroke="#fff" stroke-width="6" stroke-linejoin="round"/>
      <path d="M315 200 Q420 105 540 215" fill="none" stroke="#000" stroke-width="14"/>
      <polygon points="565,237 524,233 556,197" fill="#000"/>
    </g>
    <g class="arrow-mid-to-down">
      <path d="M695 345 Q820 420 910 300" fill="none" stroke="#fff" stroke-width="22"/>
      <polygon points="929,272 932,316 887,285" fill="#fff" stroke="#fff" stroke-width="6" stroke-linejoin="round"/>
      <path d="M695 345 Q820 420 910 300" fill="none" stroke="#000" stroke-width="14"/>
      <polygon points="928,276 929,314 891,286" fill="#000"/>
    </g>
  </svg>
</div>
</body>
</html>
```